helping new make my new business shine, with your design for : Vellaroque Fashions

Create business card for Vellaroque Fashions,( which means to shine in French)
I'm starting up a new online retail clothing store. My main voice is to sell outfit for Church and church events for men and women. (But geared more towards women)
1. photos included are from a catolog of the clothes that will be on my web site
2. Create your owns look keeping my example in mind.
3 . I want small articles of clothing on the card a few dresses, some pants, men suit
women hats, one in each corner of the card., sunglasses.all these articles are to be placed on the front of my business card to show my inventory. I want people to look at my business card and want to check out my web site.
Place each of these written out in different areas on the card clergy robes, usher uniforms, egyptian linen, men's accessories. sunglasses
4. Make your article of clothing BLING I like things that sparkle
5. On the back side will be all the contact information. The letters are to be in English or Script if you can make the business name lettering in 3D would be great but not nessassary.
Vellaroque Fashions
Order online 24/7 at: vellaroquefashions.com
Bus/Fax 505-731-6642
Mon-Wed 8:00am till 12:00 pm mst.
Lorna Whitby, Owner
lornawhitby45@quillpost.net

I'm looking forward to receiving some outstanding designs. I known the space your working with is small but when creating the women's attire and hats make them bling where possible more is better as long as it's elegant. Thank you Added Sunday, August 7, 2016

Christains women& men who take pride in what they wear to church, and who just want to look good at any high dollar event without having to spent a lot.

Fashion

The words need to be jumping out at you (3D lettering,) but ONLY if they can be done elegantly,
Vellaroque Fashions
Order online at: vellaroquefashion.com
505-731-6643
Lorna Whitby, CEO
All the contact information to be placed on the backside

Decorative
Script

• Everything I stated in the project description.
• Bling on the women attire photos and hats
• -Ok to use the photos that are attached in your business card submission (please refrain from using the model's faces, only the clothing)
• -I do not have logo but please just use the business name is a creative way
• Everything's indicated
• 1. The drawings should not use my photos but create a new look.
• 2. Do Not Use a black backing

```html
<!DOCTYPE html>
<html lang="en">
<head>
<meta charset="utf-8">
<title>Vellaroque Fashions – Business Card</title>
<link rel="stylesheet" href="https://fonts.googleapis.com/css2?family=Margarine&family=Didact+Gothic&display=swap">
<style>
  :root {
    --backing: #133f3c;
    --backing-glow: #1e5753;
    --text-dark: #141414;
    --gold: #c9a05a;
    --gold-light: #f0d9a6;
    --sparkle-light: #fbf8f1;
    --sparkle-mid: #e9dcc2;
    --sparkle-deep: #cdb58d;
    --teal: #179a8e;
    --white: #ffffff;
    --suit-grey: #3a3c40;
    --suit-light: #8a8c90;
    --dress-teal: #148e84;
  }
  html, body {
    margin: 0;
    padding: 0;
    width: 1200px;
    height: 686px;
    overflow: hidden;
    background: var(--backing);
  }
  .card {
    position: relative;
    width: 1200px;
    height: 686px;
    background: var(--backing);
    overflow: hidden;
  }
  .card-frame {
    position: absolute;
    inset: 0;
  }
  .brand-name {
    position: absolute;
    margin: 0;
    font-family: "Margarine", cursive;
    font-weight: 400;
    color: var(--teal);
    line-height: 1;
    text-align: center;
    white-space: nowrap;
  }
  .brand-name-first {
    left: 360px;
    top: 104px;
    width: 460px;
    font-size: 96px;
  }
  .brand-name-second {
    left: 376px;
    top: 254px;
    width: 440px;
    font-size: 104px;
  }
  .owner-title {
    position: absolute;
    left: 340px;
    top: 398px;
    width: 520px;
    text-align: center;
    margin: 0;
    font-family: "Didact Gothic", sans-serif;
    font-size: 56px;
    line-height: 1;
    color: var(--text-dark);
    white-space: nowrap;
  }
  .contact {
    position: absolute;
    margin: 0;
    font-family: "Didact Gothic", sans-serif;
    color: var(--white);
    line-height: 1.1;
    font-size: 35px;
    white-space: nowrap;
  }
  .contact-owner {
    left: 95px;
    top: 558px;
  }
  .contact-owner .role {
    display: block;
  }
  .contact-phone {
    left: 400px;
    top: 580px;
    width: 312px;
    text-align: center;
  }
  .contact-web {
    right: 95px;
    top: 558px;
    text-align: right;
  }
</style>
</head>
<body>
<main class="card">
  <svg class="card-frame" viewBox="0 0 1200 686" width="1200" height="686">
    <defs>
      <radialGradient id="sparkleField" cx="50%" cy="55%" r="65%">
        <stop offset="0%" stop-color="#fbf8f1"/>
        <stop offset="55%" stop-color="#e9dcc2"/>
        <stop offset="100%" stop-color="#cdb58d"/>
      </radialGradient>
      <linearGradient id="goldEdge" x1="0" y1="0" x2="1" y2="0">
        <stop offset="0%" stop-color="#c9a05a"/>
        <stop offset="50%" stop-color="#f0d9a6"/>
        <stop offset="100%" stop-color="#c9a05a"/>
      </linearGradient>
      <linearGradient id="womanTones" x1="0" y1="0" x2="0" y2="1">
        <stop offset="0%" stop-color="#1b1b1d"/>
        <stop offset="45%" stop-color="#148e84"/>
        <stop offset="100%" stop-color="#141416"/>
      </linearGradient>
      <linearGradient id="manTones" x1="0" y1="0" x2="1" y2="0">
        <stop offset="0%" stop-color="#3a3c40"/>
        <stop offset="50%" stop-color="#8a8c90"/>
        <stop offset="100%" stop-color="#3a3c40"/>
      </linearGradient>
      <radialGradient id="swirlGlow" cx="50%" cy="50%" r="50%">
        <stop offset="0%" stop-color="#1e5753"/>
        <stop offset="100%" stop-color="#133f3c"/>
      </radialGradient>
    </defs>

    <polygon class="sparkle-band" role="img" aria-label="Gold and white glitter background"
      fill="url(#sparkleField)"
      points="0,35 416,35 444,71 773,71 802,35 1200,35 1200,516 952,516 921,481 341,481 310,516 0,516"/>

    <polyline class="gold-edge-top" fill="none" stroke="url(#goldEdge)" stroke-width="4"
      points="0,35 416,35 444,71 773,71 802,35 1200,35"/>
    <polyline class="gold-edge-bottom" fill="none" stroke="url(#goldEdge)" stroke-width="4"
      points="0,516 310,516 341,481 921,481 952,516 1200,516"/>

    <rect class="feature-womens-outfit" role="img"
      aria-label="Woman's church outfit: wide black brim hat with teal bow and jewel, teal and black jacket, black clutch"
      x="6" y="48" width="334" height="466" rx="10" fill="url(#womanTones)" opacity="0.9"/>
    <rect class="feature-mens-suit" role="img"
      aria-label="Man's charcoal pinstripe suit with white shirt and pale yellow tie"
      x="962" y="68" width="212" height="446" rx="10" fill="url(#manTones)"/>

    <rect class="footer-flourish" role="img" aria-label="Faint decorative scroll flourish"
      x="450" y="560" width="300" height="126" fill="url(#swirlGlow)" opacity="0.7"/>

    <line class="footer-divider" x1="382" y1="548" x2="382" y2="652" stroke="#c9a05a" stroke-width="3"/>
    <line class="footer-divider" x1="728" y1="548" x2="728" y2="652" stroke="#c9a05a" stroke-width="3"/>
  </svg>

  <h1 class="brand-name brand-name-first">Vellaroque</h1>
  <p class="brand-name brand-name-second">Fashions</p>
  <p class="owner-title">Lorna Whitby (CEO)</p>

  <p class="contact contact-owner">Lorna Whitby<span class="role">CEO</span></p>
  <p class="contact contact-phone">505-731-6643</p>
  <p class="contact contact-web">Order online at:<br>vellaroquefashion.com</p>
</main>
</body>
</html>
```